Modern card design needed for building development company

We are looking for a sharp modern new look for our business cards.
We are a New Zealand based company called TKV Ventures NZ LTD that specialises in subdividing large sections, housing and commercial buildings.
We have attached a photo of the current logo and would like to see it improved somehow as it looks a bit dated.
We are open to any colours.

Target Market(s)

Investors, Property buyers

Industry/Entity Type

Investment

Contact Information for Business Card

TKV VENTURES NZ LTD
www.tkvventuresnz.co.nz

Howard Pennick
Phone +64 21 843 192
Email hdpennick@fernmail.co.nz

Font styles to use
Serif
Sans Serif

Colors
0792cd
33a6d7
85cae6
6b449b
886aae
f04a50
ec1f27
f37122
f68d4d

Requirements
Must have
• Please try and make the logo more modern or if you have a similar one we would like to see it.

```html
<!DOCTYPE html>
<html lang="en">
<head>
<meta charset="utf-8">
<title>TKV Ventures NZ LTD – Business Card</title>
<link href="https://fonts.googleapis.com/css2?family=Montserrat:wght@500;700&family=Work+Sans:wght@400&display=swap" rel="stylesheet">
<style>
  :root {
    --backdrop: #2a2a2a;
    --card: #1c1c1c;
    --ink: #f2f2f2;
    --ink-soft: #cfcfcf;
    --rule: #d8d8d8;
    --foil: #bdbdbd;
  }
  * { box-sizing: border-box; margin: 0; padding: 0; }
  html, body {
    width: 1200px; height: 900px; overflow: hidden;
    background: var(--backdrop);
  }
  .canvas { position: relative; width: 1200px; height: 900px; }
  .card {
    position: absolute; left: 240px; width: 720px; height: 400px;
    background: var(--card);
    box-shadow: 0 14px 30px rgba(0,0,0,0.45);
  }
  .card--front { top: 40px; }
  .card--back { top: 460px; }

  .brand {
    font-family: "Montserrat", sans-serif; font-weight: 700;
    letter-spacing: 0.08em; text-transform: uppercase;
    display: flex; align-items: center; gap: 12px;
  }
  .brand__mark { width: 16px; height: 16px; border: 2px solid currentColor; }
  .card--front .brand {
    position: absolute; left: 0; right: 0; top: 0; bottom: 0;
    justify-content: center; color: var(--foil); font-size: 24px;
  }
  .card--back .brand {
    position: absolute; right: 56px; top: 108px;
    color: var(--ink); font-size: 18px;
  }

  .person { position: absolute; left: 56px; top: 100px; }
  .person__name {
    font-family: "Montserrat", sans-serif; font-weight: 700;
    font-size: 26px; color: var(--ink); letter-spacing: 0.02em;
  }
  .person__role {
    font-family: "Work Sans", sans-serif; font-size: 15px;
    color: var(--ink-soft); margin-top: 2px;
  }
  .divider {
    position: absolute; left: 48px; right: 56px; top: 210px;
    height: 1.5px; background: var(--rule);
  }
  .contact {
    position: absolute; left: 48px; top: 236px; list-style: none;
    font-family: "Work Sans", sans-serif; font-size: 17px; color: var(--ink);
  }
  .contact li { display: flex; align-items: center; gap: 14px; height: 28px; }
  .contact svg { width: 13px; height: 13px; fill: none; stroke: var(--ink-soft); stroke-width: 1.6; }
  .address {
    position: absolute; right: 56px; bottom: 48px; text-align: right;
    font-family: "Work Sans", sans-serif; font-size: 19px;
    color: var(--ink-soft); line-height: 1.35;
  }
</style>
</head>
<body>
<main class="canvas">
  <section class="card card--front">
    <div class="brand"><span class="brand__mark"></span>TKV Ventures NZ LTD</div>
  </section>

  <section class="card card--back">
    <div class="person">
      <h1 class="person__name">HOWARD PENNICK</h1>
      <p class="person__role">Director</p>
    </div>
    <div class="brand"><span class="brand__mark"></span>TKV Ventures NZ LTD</div>
    <div class="divider"></div>
    <ul class="contact">
      <li>
        <svg viewBox="0 0 16 16" aria-hidden="true"><path d="M4 1.5l2.5 3-1.5 2c1 2 2.5 3.5 4.5 4.5l2-1.5 3 2.5-1.5 2.5C7 15 1 9 1.5 3z"/></svg>
        +64 21 843 192
      </li>
      <li>
        <svg viewBox="0 0 16 16" aria-hidden="true"><rect x="1.5" y="3.5" width="13" height="9"/><path d="M1.5 3.5L8 9l6.5-5.5"/></svg>
        hdpennick@fernmail.co.nz
      </li>
      <li>
        <svg viewBox="0 0 16 16" aria-hidden="true"><circle cx="8" cy="8" r="6.5"/><path d="M1.5 8h13M8 1.5c-3 3.5-3 9.5 0 13M8 1.5c3 3.5 3 9.5 0 13"/></svg>
        www.tkvventuresnz.co.nz
      </li>
    </ul>
    <p class="address">PO BOX 51824 Devonport<br>Auckland New Zealand</p>
  </section>
</main>
</body>
</html>
```